Bright Harbor Counseling Letterhead for hip modern business

I would like some ombre use of the colors in the logo hip letterhead that incorporates logo colors and feel, needs to connect with young professionals and college students. i need to be able to write letters to schools to excuse absences as well. i like color blocks on one side preferably using colors from the attached logo design.

Target Market(s)

high income young people, young adults and college students

Industry/Entity Type

mental health

Font styles to use
Serif
Sans Serif

Colors
0054AA
0677BA
7BADD7
CADEEF
E8F1F8
0094D4
00A9DD
6FCCEA
C7EBF8
E9F6FB
00AB8E
00BBA5
67D7C9
C6EFE9
E9F9F6
59FF00
82FF00
B8FF75
E3FFCB
F4FFEA
A7469A
B969AE
D3A5CF
EDDBEB
F8F0F9
6B429C
8869AF
B7A5CE
E3DAEB
F3F0F8

Requirements
Must have
• a modern hip feel, somewhat color

```html
<!DOCTYPE html>
<html lang="en">
<head>
<meta charset="UTF-8">
<title>Bright Harbor Counseling Letterhead</title>
<link rel="stylesheet" href="https://fonts.googleapis.com/css2?family=Questrial&display=swap">
<style>
  :root {
    --paper-light: #f3f3f3;
    --paper-dark: #e1e1e1;
    --ink: #2b2b2b;
    --ink-soft: #3a3a3a;
    --blue: #3a77c2;
    --plum: #8e2c7b;
    --accent-purple: #8869af;
  }
  * { margin: 0; padding: 0; box-sizing: border-box; }
  html, body {
    width: 960px; height: 1200px; overflow: hidden;
    background: #bdbdbd;
  }
  .letterhead {
    position: relative;
    width: 960px; height: 1200px;
    background: linear-gradient(90deg, var(--paper-light), var(--paper-dark));
    font-family: "Questrial", "Century Gothic", sans-serif;
    color: var(--ink);
  }
  .brand {
    position: absolute; left: 88px; top: 110px;
    color: var(--ink);
  }
  .brand-name {
    font-size: 38px; line-height: 1; letter-spacing: 0.5px;
    display: flex; align-items: center; gap: 10px;
  }
  .brand-dot {
    width: 16px; height: 16px; border-radius: 50%;
    background: var(--accent-purple);
  }
  .brand-sub {
    font-size: 19px; letter-spacing: 2.5px;
    margin-top: 6px; padding-left: 88px;
  }
  .contact {
    position: absolute; left: 633px; top: 68px;
    border-left: 1.5px solid var(--blue);
    padding-left: 26px; height: 102px;
    font-size: 15px; line-height: 17.5px; color: var(--ink);
  }
  .contact-row { display: flex; align-items: flex-start; gap: 8px; }
  .contact-row + .contact-row { margin-top: 0; }
  .contact-row.address { margin-bottom: 5px; }
  .contact-icon { width: 11px; height: 11px; flex: none; margin-top: 3px; fill: var(--blue); }
  .salutation {
    position: absolute; left: 88px; top: 355px;
    font-size: 21px; color: var(--ink);
  }
  .letter-body {
    position: absolute; left: 88px; top: 412px; width: 790px;
    font-size: 13.6px; line-height: 20.5px; color: var(--ink-soft);
    text-align: justify;
  }
  .letter-body p + p { margin-top: 20px; }
  .closing {
    position: absolute; left: 88px; top: 804px;
    font-size: 13.6px; color: var(--ink-soft);
  }
  .signature {
    position: absolute; left: 88px; top: 840px;
    width: 126px; height: 68px;
    background: linear-gradient(90deg, rgba(40,40,40,0.18), rgba(40,40,40,0.08));
    border-radius: 4px;
  }
  .footer-band {
    position: absolute; left: 0; bottom: 0;
    width: 100%; height: 22px;
    background: var(--plum);
  }
</style>
</head>
<body>
<main class="letterhead">
  <header>
    <div class="brand">
      <div class="brand-name">Bright Harbor <span class="brand-dot"></span></div>
      <div class="brand-sub">Counseling</div>
    </div>
    <address class="contact" style="font-style:normal">
      <div class="contact-row address">
        <svg class="contact-icon" viewBox="0 0 12 12"><path d="M6 0a4 4 0 0 0-4 4c0 3 4 8 4 8s4-5 4-8a4 4 0 0 0-4-4zm0 5.6A1.6 1.6 0 1 1 6 2.4a1.6 1.6 0 0 1 0 3.2z"/></svg>
        <span>214 Willowmere Court<br>Fairview, Oregon 97024</span>
      </div>
      <div class="contact-row">
        <svg class="contact-icon" viewBox="0 0 12 12"><path d="M2.4 0.5l2 2.2-1 1.4c.7 1.6 1.9 2.8 3.5 3.5l1.4-1 2.2 2-1.2 2.6C5 11 1 7 .2 1.7z"/></svg>
        <span>555-210-4471</span>
      </div>
      <div class="contact-row">
        <svg class="contact-icon" viewBox="0 0 12 12"><path d="M3 1h6v3H3zM1 4.5h10v5H9V8H3v1.5H1zM3 8.6h6V11H3z"/></svg>
        <span>555-210-4472</span>
      </div>
      <div class="contact-row">
        <svg class="contact-icon" viewBox="0 0 12 12"><path d="M1 2.5h10v7H1zM1.6 3l4.4 3.4L10.4 3"/></svg>
        <span>hello@brightharbor.example</span>
      </div>
      <div class="contact-row">
        <svg class="contact-icon" viewBox="0 0 12 12"><circle cx="6" cy="6" r="5.5"/></svg>
        <span>www.brightharbor.example</span>
      </div>
    </address>
  </header>

  <h1 class="salutation" style="font-weight:400">Dear Mr. Alder,</h1>

  <section class="letter-body">
    <p>Lorem ipsum dolor sit amet, consectetur adipiscing elit. Donec orci purus, luctus vitae dignissim eu, iaculis sed purus. Vivamus faucibus, ipsum nec aliquet viverra, leo mauris condimentum ligula, sit amet sagittis enim ligula quis arcu. Nam egestas tortor id nisi porttitor mattis. In tortor ante, ultricies in suscipit a, tempus non massa. Vivamus et auctor mi. Fusce vel massa nulla. Phasellus nec eros mauris, et scelerisque orci.</p>
    <p>Donec malesuada orci vitae nulla accumsan porta a id massa. Quisque accumsan iaculis magna sit amet fringilla. Maecenas consequat, magna eget tincidunt semper, odio nibh rutrum mi, id feugiat ante nisi eu risus. Vestibulum nunc orci, rhoncus a placerat in, ultricies in mi. Cras mattis varius eros, vel fringilla nisi suscipit eget. Quisque scelerisque sagittis nulla at porttitor.</p>
    <p>Sed id augue vitae urna euismod commodo aliquet a quam. Pellentesque arcu velit, cursus et malesuada ut, consequat et diam. Nullam erat sem, rhoncus id ullamcorper vitae, rhoncus et arcu. In ultricies ultricies nulla, ut rutrum nisi iaculis at. Donec eu magna a metus ornare faucibus. Fusce aliquet faucibus ultricies. Morbi semper, est id tincidunt gravida, sem arcu adipiscing lacus, ac bibendum nulla leo eu purus. Quisque nec diam sed risus consectetur a ccumsan quis quis nibh. Vestibulum id purus lorem.</p>
    <p>It is a long established fact that a reader will be distracted by the readable content of a page when looking at its layout. The point of using Lorem Ipsum is that it has a more-or-less normal distribution of letters, as opposed to using 'Content here, content here', making it look like readable English. Many desktop publishing packages</p>
  </section>

  <p class="closing">Sincerely,</p>
  <div class="signature" role="img" aria-label="Handwritten signature of the letter's author"></div>

  <div class="footer-band"></div>
</main>
</body>
</html>
```